Geschäftspapiere für Handwerksunternehmen
Zielgruppe
Handwerk
Elektroinstallation
Design Modern
Aufgabenstellung
Anschrift, Kontaktdaten, Bankverbindung, Logo,
Im Birkengrund 9 74315 Salem Inhaber Lothar Brenning
Telefon: 07341-5526318 Email: info@tavo-stromtechnik.de Internet: www.tavo-stromtechnik.de
Finanzamt Norddorf USt.-ID: DE574163028 Steuer Nr.:3958402761
Kreiskasse Feldau IBAN:DE71482093160007319455 BIC:KRFEDEX2FDL

```html
<!DOCTYPE html>
<html lang="de">
<head>
<meta charset="utf-8">
<title>Tavo Stromtechnik – Geschäftspapiere</title>
<link href="https://fonts.googleapis.com/css2?family=Montserrat:wght@400;600;700&display=swap" rel="stylesheet">
<style>
  :root{
    --bg:#e3e4e8;
    --ink:#0a0a0a;
    --ink-soft:#141414;
    --volt:#ece51d;
    --volt-faint:#f6f3c8;
    --paper:#f4f5f7;
    --steel-hi:#c9c9c9;
    --steel-lo:#6f6f6f;
    --muted:#b8b8b8;
  }
  *{box-sizing:border-box;margin:0;padding:0}
  html,body{width:1200px;height:927px;overflow:hidden;background:var(--bg);font-family:"Montserrat",sans-serif}
  .canvas{position:relative;width:1200px;height:927px}
  .piece{position:absolute;overflow:hidden}
  .brand{display:flex;align-items:center;gap:4px;color:var(--volt);font-weight:700;white-space:nowrap;line-height:1}
  .brand .dot{border:2px solid var(--volt);border-radius:50%;flex:none}

  /* business card front */
  .card-front{left:126px;top:232px;width:178px;height:102px;background:var(--ink)}
  .steel{position:absolute;left:0;right:0;height:7px;background:linear-gradient(180deg,var(--steel-hi),var(--steel-lo))}
  .steel.top{top:0}.steel.bottom{bottom:0}
  .card-front .brand{position:absolute;left:0;right:0;top:38px;justify-content:center;font-size:10px}
  .card-front .brand .dot{width:14px;height:14px}
  .card-front .tagline{position:absolute;left:0;right:0;top:76px;text-align:center;color:var(--muted);font-size:4px;line-height:1.3;white-space:nowrap}

  /* business card back */
  .card-back{left:126px;top:364px;width:178px;height:103px;background:var(--ink)}
  .card-back .steel.top{width:70px;right:auto}
  .card-back .brand.vertical{position:absolute;left:30px;top:88px;transform:rotate(-90deg);transform-origin:left top;font-size:7px}
  .card-back .brand.vertical .dot{width:9px;height:9px;border-width:1.5px}
  .card-back .panel{position:absolute;left:70px;top:5px;right:0;bottom:5px;background:var(--ink-soft);border-radius:0 0 0 6px;border-left:1px solid #2a2a2a;padding:18px 0 0 8px;color:#d8d8d8}
  .card-back .name{font-size:5.6px;font-weight:700;letter-spacing:.1px}
  .card-back .role{font-size:4px;color:var(--muted);margin-top:1px}
  .contact-list{list-style:none;margin-top:16px}
  .contact-list li{display:flex;align-items:flex-start;gap:4px;font-size:4px;line-height:1.3;margin-bottom:3px;color:#cfcfcf;white-space:nowrap}
  .contact-list svg{width:7px;height:7px;flex:none}

  /* letterhead */
  .letterhead{left:357px;top:201px;width:321px;height:456px;background:var(--paper)}
  .letterhead .brand{position:absolute;left:30px;top:58px;font-size:12px}
  .letterhead .brand .dot{width:16px;height:16px}
  .watermark{position:absolute;border-radius:50%}
  .letterhead .watermark{left:78px;top:100px;width:170px;height:170px;border:16px solid var(--volt-faint)}
  .letterhead .footer-text{position:absolute;left:8px;top:427px;color:#fff;font-size:4.2px;font-weight:600;line-height:1.4;white-space:nowrap}
  .letterhead .footer-address{position:absolute;left:150px;top:428px;width:86px;text-align:center;font-size:4.6px;font-weight:700;line-height:1.3;color:var(--ink);white-space:nowrap}
  .letterhead .footer-web{position:absolute;right:5px;top:440px;font-size:5.6px;color:var(--ink);white-space:nowrap}
  .letterhead .footer-web span{color:var(--volt)}

  /* envelope C5 */
  .envelope{left:358px;top:690px;width:349px;height:180px;background:var(--paper)}
  .envelope .brand{position:absolute;left:0;right:0;top:14px;justify-content:center;font-size:9px}
  .envelope .brand .dot{width:12px;height:12px}

  /* DL envelope */
  .dl-envelope{left:762px;top:200px;width:353px;height:180px;background:var(--ink)}
  .dl-envelope .brand{position:absolute;left:30px;top:42px;font-size:9px}
  .dl-envelope .brand .dot{width:12px;height:12px}
  .dl-envelope .address{position:absolute;left:26px;top:110px;color:#e8e8e8;font-size:4.6px;line-height:1.4;white-space:nowrap}
  .dl-envelope .rule{width:64px;height:1px;background:#e8e8e8;margin:3px 0}
  .dl-envelope .watermark{left:240px;top:28px;width:100px;height:100px;border:12px solid #262626}

  /* folder */
  .folder{left:768px;top:403px;width:353px;height:465px;background:var(--ink)}
  .folder .logo-field{position:absolute;left:84px;top:194px;width:186px;height:68px;background:#0f0f0f;display:flex;align-items:center;justify-content:center}
  .folder .brand{font-size:16px;gap:6px}
  .folder .brand .dot{width:24px;height:24px;border-width:3px}
</style>
</head>
<body>
<main class="canvas">

  <section class="piece card-front" aria-label="Visitenkarte Vorderseite">
    <div class="steel top"></div>
    <div class="brand"><span class="dot"></span>Tavo Stromtechnik</div>
    <p class="tagline">Ihr Partner für Elektroinstallation<br>Licht | Kraft | Smart Home</p>
    <div class="steel bottom"></div>
  </section>

  <section class="piece card-back" aria-label="Visitenkarte Rückseite">
    <div class="steel top"></div>
    <div class="brand vertical"><span class="dot"></span>Tavo Stromtechnik</div>
    <div class="panel">
      <p class="name">LOTHAR BRENNING</p>
      <p class="role">Inhaber</p>
      <ul class="contact-list">
        <li><svg viewBox="0 0 10 10"><circle cx="5" cy="5" r="4.3" fill="none" stroke="#ece51d"/><path d="M3.4 3c.3 1.8 1.6 3.2 3.4 3.6l.4-.9-1-.5-.5.5c-.7-.3-1.2-.9-1.5-1.5l.5-.5-.5-1z" fill="#ece51d"/></svg>07341-5526318</li>
        <li><svg viewBox="0 0 10 10"><circle cx="5" cy="5" r="4.3" fill="none" stroke="#ece51d"/><circle cx="5" cy="5" r="1.8" fill="#ece51d"/></svg>info@tavo-stromtechnik.de<br>www.tavo-stromtechnik.de</li>
        <li><svg viewBox="0 0 10 10"><path d="M5 1a3 3 0 0 0-3 3c0 2.2 3 5 3 5s3-2.8 3-5a3 3 0 0 0-3-3z" fill="#ece51d"/><circle cx="5" cy="4" r="1" fill="#141414"/></svg>Im Birkengrund 9<br>74315 Salem</li>
      </ul>
    </div>
    <div class="steel bottom"></div>
  </section>

  <section class="piece letterhead" aria-label="Briefbogen">
    <svg width="321" height="456" style="position:absolute;left:0;top:0">
      <path d="M262 0 C276 0 280 30 296 30 L321 30 L321 0 Z" fill="#0a0a0a"/>
      <path d="M0 413 L128 413 C136 413 140 450 154 452 L321 452 L321 456 L0 456 Z" fill="#0a0a0a"/>
      <path d="M138 424 L236 424 L248 448 L150 448 Z" fill="#ece51d"/>
    </svg>
    <div class="brand"><span class="dot"></span>Tavo Stromtechnik</div>
    <div class="watermark" role="img" aria-label="Blasse Markenfläche als Hintergrundmotiv"></div>
    <p class="footer-text">Finanzamt Norddorf - USt.-ID: DE574163028<br>Kreiskasse Feldau - BIC: KRFEDEX2FDL<br>Tel: 07341-5526318 - info@tavo-stromtechnik.de</p>
    <p class="footer-address">Im Birkengrund 9<br>74315 Salem</p>
    <p class="footer-web">www.<span>tavo-stromtechnik</span>.de</p>
  </section>

  <section class="piece envelope" aria-label="Briefumschlag">
    <svg width="349" height="180" style="position:absolute;left:0;top:0">
      <path d="M0 0 L349 0 L349 46 C349 52 344 55 336 55 L16 55 C8 55 4 50 3 44 Z" fill="#0a0a0a"/>
    </svg>
    <div class="brand"><span class="dot"></span>Tavo Stromtechnik</div>
  </section>

  <section class="piece dl-envelope" aria-label="Langumschlag">
    <div class="brand"><span class="dot"></span>Tavo Stromtechnik</div>
    <div class="address">
      <p>Im Birkengrund 9<br>74315 Salem</p>
      <div class="rule"></div>
      <p>Tel: 07341-5526318<br>Email: info@tavo-stromtechnik.de<br>Website: www.tavo-stromtechnik.de</p>
    </div>
    <div class="watermark" role="img" aria-label="Dunkle Markenfläche als Hintergrundmotiv"></div>
  </section>

  <section class="piece folder" aria-label="Präsentationsmappe">
    <div class="logo-field">
      <div class="brand"><span class="dot"></span>Tavo Stromtechnik</div>
    </div>
  </section>

</main>
</body>
</html>
```